Residential building / Apartments for sale landing page

I need a website / landing page design for my latest development project - a residential building with 70+ apartments for sale. I need the design in layers in Photoshop/Illustrator/InDesign format with all the icons/shapes/maps/graphic assets in vector format (svg, ai, eps) as much as possible.

I prefer white website and please consider the performance/coding experience. We're not making something suitable only for a design contest with fancy parallax effects and confusing animations. We're trying to create usable and clean UI with good UX.

The website will be custom coded, i.e. I'm not using WordPress.

I know that the existing 3D photos are not good but for now you can use them or replace them with some stock photos. I'm going to create new 3D photos soon.

Industry/Entity Type

Real Estate Development

Number of Pages Required

1 page

```html
<!DOCTYPE html>
<html lang="en">
<head>
<meta charset="utf-8">
<title>Pine Ridge – Apartments for Sale</title>
<link href="https://fonts.googleapis.com/css2?family=Montserrat:wght@400;500;600;700;800&display=swap" rel="stylesheet">
<style>
:root{
  --green:#8cc63f;
  --green-dark:#76b02e;
  --ink:#1d1f22;
  --text:#555a60;
  --muted:#8a8f95;
  --line:#e6e8ea;
  --soft:#f7f8f8;
  --footer:#25282d;
  --white:#ffffff;
}
*{box-sizing:border-box;margin:0;padding:0}
html,body{width:1200px;height:4655px;overflow:hidden}
body{font-family:"Montserrat",sans-serif;color:var(--ink);background:var(--white);position:relative}
.abs{position:absolute}
.btn{position:absolute;background:var(--green);color:var(--white);font-weight:700;display:flex;align-items:center;justify-content:center;letter-spacing:.5px}

/* header */
.site-header{position:absolute;left:0;top:0;width:1200px;height:121px;background:var(--white)}
.brand{position:absolute;left:88px;top:40px;display:flex;align-items:center;gap:10px;font-weight:800;font-size:22px;color:var(--ink)}
.brand-mark{width:16px;height:16px;background:var(--green)}
.nav{position:absolute;top:63px;left:394px;display:flex;gap:38px;font-size:13px;font-weight:500}
.nav a{color:var(--ink);text-decoration:none}
.nav a.active{color:var(--green);border-bottom:2px solid var(--green);padding-bottom:8px}
.header-cta{left:983px;top:52px;width:143px;height:44px;font-size:12px;font-weight:600;gap:10px}
.flag{width:18px;height:12px;background:var(--white);position:relative}
.flag::before{content:"";position:absolute;left:7px;top:0;width:4px;height:12px;background:#c8102e}
.flag::after{content:"";position:absolute;left:0;top:4px;width:18px;height:4px;background:#c8102e}

/* hero */
.hero{position:absolute;left:0;top:121px;width:1200px;height:690px;background:linear-gradient(180deg,#3b4046 0%,#2c3135 45%,#1f2326 100%)}
.hero-eyebrow{position:absolute;top:210px;width:100%;text-align:center;color:var(--white);font-size:36px;letter-spacing:18px;font-weight:400}
.hero-rule{position:absolute;left:367px;width:462px;height:3px;background:var(--green)}
.hero-title{position:absolute;top:268px;width:100%;text-align:center;color:var(--white);font-size:66px;font-weight:800;letter-spacing:1px}
.hero-sub{position:absolute;top:383px;width:100%;text-align:center;color:var(--white);font-size:17px;letter-spacing:3px}
.hero-price{position:absolute;top:434px;width:100%;text-align:center;color:var(--white);font-size:30px;font-weight:400}
.hero-cta{left:490px;top:510px;width:217px;height:50px;font-size:16px}

/* about */
.about{position:absolute;left:0;top:811px;width:1200px;height:445px;background:var(--white)}
.about-frame{position:absolute;left:83px;top:64px;width:340px;height:319px;border:4px solid var(--green)}
.about-photo{position:absolute;left:105px;top:82px;width:343px;height:318px;background:linear-gradient(135deg,#6f8f5a,#c9d6c2 55%,#4d6a3c);box-shadow:0 10px 24px rgba(0,0,0,.18)}
.section-title{font-weight:800;color:var(--ink);letter-spacing:.5px}
.about-title{position:absolute;left:591px;top:128px;font-size:44px}
.about-text{position:absolute;left:590px;top:200px;width:500px;font-size:14px;line-height:26px;color:var(--text)}
.about-cta{left:589px;top:311px;width:114px;height:29px;font-size:13px}

/* facilities */
.facilities{position:absolute;left:0;top:1256px;width:1200px;height:690px;background:linear-gradient(180deg,var(--white),var(--soft))}
.fac-title{position:absolute;left:92px;top:75px;font-size:46px}
.fac-sub{position:absolute;left:96px;top:143px;font-size:17px;color:var(--ink)}
.fac-rule{position:absolute;left:92px;top:208px;width:1040px;height:1px;background:var(--line)}
.fac-list{position:absolute;left:95px;top:264px;list-style:none}
.fac-list li{font-size:14px;color:var(--text);height:34.2px;display:flex;align-items:center}
.fac-list li::before{content:"";width:8px;height:8px;background:var(--green);margin-right:22px}
.thumb{position:absolute;box-shadow:0 4px 12px rgba(0,0,0,.2)}
.plan-frame{position:absolute;left:799px;top:262px;width:339px;height:320px;border:4px solid var(--green)}
.plan{position:absolute;left:772px;top:273px;width:343px;height:327px;background:linear-gradient(135deg,#ffffff,#eef0f2 60%,#dfe3e7);box-shadow:0 6px 18px rgba(0,0,0,.18)}

/* construction */
.construction{position:absolute;left:0;top:1946px;width:1200px;height:578px;background:linear-gradient(120deg,var(--green) 0%,#93cb47 50%,var(--green-dark) 100%)}
.con-title{position:absolute;left:83px;top:94px;font-size:44px;color:var(--white)}
.con-sub{position:absolute;left:83px;top:152px;font-size:17px;color:var(--white)}
.con-list{position:absolute;left:83px;top:238px;list-style:none}
.con-list li{height:30.7px;display:flex;align-items:center;font-size:13.5px;font-weight:500;color:var(--white);white-space:nowrap}
.con-list li::before{content:"";width:7px;height:7px;background:var(--white);margin-right:26px}
.con-list b{background:var(--white);color:var(--ink);font-weight:600;padding:1px 6px;margin-right:8px}

/* map */
.map{position:absolute;left:0;top:2524px;width:1200px;height:282px;background:linear-gradient(180deg,#f2f3f4,#e9ebec)}
.map-pin{position:absolute;left:565px;top:101px;width:66px;height:66px;border-radius:50%;background:#111;display:flex;align-items:center;justify-content:center}

/* gallery */
.gallery-title{position:absolute;top:2890px;width:1200px;text-align:center;font-size:44px}
.gallery-sub{position:absolute;top:2962px;width:1200px;text-align:center;font-size:17px}
.tile{position:absolute;overflow:hidden}
.tile-label{position:absolute;left:17px;bottom:50px;color:var(--white);font-weight:800;font-size:21px}
.tile-view{position:absolute;left:17px;bottom:30px;color:var(--white);font-size:13px}
.tile-overlay{position:absolute;inset:0;background:rgba(140,198,63,.82)}

/* contact */
.contact-title{position:absolute;left:112px;top:3835px;font-size:44px}
.contact-text{position:absolute;left:113px;top:3910px;width:400px;font-size:17px;line-height:26px}
.contact-info{position:absolute;left:149px;font-size:13.5px;line-height:26px;color:var(--text)}
.icon{position:absolute;left:113px}
.field{position:absolute;left:598px;width:472px;border:2px solid var(--green);font-size:13.5px;color:var(--text);padding:18px 20px}
.send-cta{left:598px;top:4133px;width:472px;height:59px;font-size:16px}

/* footer */
.footer{position:absolute;left:0;top:4326px;width:1200px;height:329px;background:var(--footer);color:#d7dadd}
.footer .brand{left:88px;top:70px;color:var(--white)}
.footer-text{position:absolute;left:88px;top:150px;width:330px;font-size:12px;line-height:23px}
.copyright{position:absolute;left:88px;top:248px;font-size:11px}
.footer-head{position:absolute;top:72px;font-size:19px;font-weight:600;color:var(--white)}
.quick{position:absolute;left:536px;top:132px;list-style:none;font-size:12px}
.quick li{height:25.6px}
.footer-contact{position:absolute;left:836px;top:130px;font-size:11.5px;line-height:20px}
</style>
</head>
<body>

<header class="site-header">
  <div class="brand"><span class="brand-mark"></span>PINE RIDGE</div>
  <nav class="nav">
    <a class="active" href="#">Pine Ridge</a><a href="#">The project</a><a href="#">Apartments/Sales</a><a href="#">Location</a><a href="#">Gallery</a>
  </nav>
  <div class="btn header-cta">Contact | EN <span class="flag"></span></div>
</header>

<section class="hero" role="img" aria-label="Aerial render of the residential building on a hillside street at dusk">
  <div class="hero-eyebrow">SALE OF</div>
  <div class="hero-rule" style="top:269px"></div>
  <div class="hero-title">APARTMENTS</div>
  <div class="hero-rule" style="top:360px"></div>
  <div class="hero-sub">directly from the investor with 10% discount</div>
  <div class="hero-price">Price from € 2,054,000/m2</div>
  <div class="btn hero-cta">BUY NOW</div>
</section>

<section class="about">
  <div class="about-frame"></div>
  <div class="about-photo" role="img" aria-label="Render of the building facade with green terraces"></div>
  <h2 class="section-title about-title">ABOUT US</h2>
  <p class="about-text">Lorem ipsum, or lipsum as it is sometimes known, is dummy text used in laying out print, graphic or web designs. The passage is attributed to an unknown typesetter in the 15th century who is though</p>
  <div class="btn about-cta">VIEW MORE</div>
</section>

<section class="facilities">
  <h2 class="section-title fac-title">FACILITIES / BENEFITS</h2>
  <p class="fac-sub">Lorem ipsum, or lipsum as it is sometimes known, is dummy text</p>
  <div class="fac-rule"></div>
  <ul class="fac-list">
    <li>Green areas and gardens</li><li>Parking spaces</li><li>Bicycleparking</li><li>Outsideworkoutarea</li><li>NFC controlledaccess</li><li>OutdoorYogaarea</li><li>Relaxationarea</li><li>Childrens playground</li><li>Pool</li><li>Restaurant</li>
  </ul>
  <div class="thumb" style="left:513px;top:455px;width:107px;height:107px;background:linear-gradient(135deg,#7a7e78,#a9ada4,#5d6258)" role="img" aria-label="Aerial photo of the site"></div>
  <div class="thumb" style="left:634px;top:403px;width:107px;height:108px;background:#4f7d2a;display:flex;align-items:center;justify-content:center;color:#fff;font-weight:700;font-size:13px">PINE RIDGE</div>
  <div class="thumb" style="left:634px;top:528px;width:107px;height:72px;background:linear-gradient(135deg,#5f8a3d,#a9c58e)" role="img" aria-label="Aerial render of the garden courtyard"></div>
  <div class="plan-frame"></div>
  <div class="plan" role="img" aria-label="Floor plan of sections A, B and C"></div>
</section>

<section class="construction">
  <h2 class="section-title con-title">CONSTRUCTION FEATURES</h2>
  <p class="con-sub">Lorem ipsum, or lipsum as it is sometimes known, is dummy text</p>
  <ul class="con-list">
    <li><b>Veltra Windows</b>5 chamber noise reducing glazing with high temperature and noise insulation efficiency</li>
    <li><b>Claymark bricks</b>Austrian Claymark Thermabrick bricks with porous system and 25 cm thick outer walls</li>
    <li><b>HighCeilings</b>2.70m high ceilings giving the light and space you need</li>
    <li><b>ThermalInsulation System Kalvor</b>Kalvor Silicone Plaster Thermal Insulation System 10 cm thick and 15 cm thick from the north walls</li>
    <li><b>Air conditioners</b>All air conditioners piping systems are installed - ready to plug in the inside and outside body of the aircon system</li>
    <li><b>HPL ventilatedfacadeLamiplan</b>Suspended ventilated facade with highly pressed laminated panels by Lamiplan in wood color</li>
    <li><b>PanoramicLifteraliftsoverlookingthepark</b>Giving you the everyday glimpse over the inside garden and putting a smile on your face</li>
    <li><b>WaterproofingwithPVC membraneAquashield</b>PVC membrane with high puncture and tear resistance, UV resistance and vapor permeability</li>
  </ul>
</section>

<section class="map" role="img" aria-label="Street map showing the building location">
  <div class="map-pin">
    <svg width="24" height="30" viewBox="0 0 24 30"><path d="M12 0C5.4 0 0 5.3 0 11.8 0 20 12 30 12 30s12-10 12-18.2C24 5.3 18.6 0 12 0z" fill="#fff"/><circle cx="12" cy="11.5" r="4.5" fill="#111"/></svg>
  </div>
</section>

<h2 class="section-title gallery-title">GALLERY</h2>
<p class="gallery-sub">Lorem ipsum, or lipsum as it is sometime</p>
<div class="tile" style="left:116px;top:3050px;width:233px;height:488px;background:linear-gradient(180deg,#eceae6,#b9b6b0 55%,#4a4540)" role="img" aria-label="Living room interior with grey sofa">
  <div class="tile-label">APRIL 2021</div><div class="tile-view">View</div>
</div>
<div class="tile" style="left:358px;top:3050px;width:488px;height:488px;background:linear-gradient(180deg,#f4f4f2,#d6d5d2 55%,#5a4436)" role="img" aria-label="Bright living room with large windows and wooden floor">
  <div class="tile-label">MARCH 2021</div><div class="tile-view">View</div>
</div>
<div class="tile" style="left:855px;top:3050px;width:233px;height:240px;background:linear-gradient(180deg,#8d9bab,#c9c0b2 60%,#5b4d42)" role="img" aria-label="Bedroom interior"></div>
<div class="tile" style="left:855px;top:3299px;width:233px;height:239px;background:linear-gradient(180deg,#d9d6d0,#8c8478)" role="img" aria-label="Apartment interior">
  <div class="tile-overlay"></div>
  <svg class="abs" style="left:176px;top:26px" width="30" height="30" viewBox="0 0 30 30"><circle cx="12" cy="12" r="9" fill="none" stroke="#fff" stroke-width="2"/><line x1="19" y1="19" x2="27" y2="27" stroke="#fff" stroke-width="2"/></svg>
  <div class="tile-label">FEBRUARY 2021</div><div class="tile-view">View</div>
</div>

<h2 class="section-title contact-title">CONTACT</h2>
<p class="contact-text">Lorem ipsum, or lipsum as it is sometime<br>s known, is dummy text</p>
<svg class="icon" style="top:4022px" width="16" height="18" viewBox="0 0 16 18"><path d="M8 1C4.7 1 2 3.6 2 6.8 2 11 8 17 8 17s6-6 6-10.2C14 3.6 11.3 1 8 1z" fill="none" stroke="var(--green)" stroke-width="1.5"/><circle cx="8" cy="7" r="2" fill="var(--green)"/></svg>
<div class="contact-info" style="top:4015px">Pine Ridge<br>Company Reg: REG-804.217.553<br>Office: Larchweg 14,&nbsp; Talbach, Alpland</div>
<svg class="icon" style="top:4120px" width="18" height="18" viewBox="0 0 18 18"><path d="M4 1l3 4-2 2c1 2 3 4 5 5l2-2 4 3-2 3C8 16 2 10 1 4z" fill="none" stroke="var(--green)" stroke-width="1.5"/></svg>
<div class="contact-info" style="top:4116px">+00 482 55170</div>
<svg class="icon" style="top:4146px" width="18" height="18" viewBox="0 0 18 18"><circle cx="9" cy="9" r="7.5" fill="none" stroke="var(--green)" stroke-width="1.5"/><ellipse cx="9" cy="9" rx="3.2" ry="7.5" fill="none" stroke="var(--green)" stroke-width="1.2"/><line x1="1.5" y1="9" x2="16.5" y2="9" stroke="var(--green)" stroke-width="1.2"/></svg>
<div class="contact-info" style="top:4141px;color:var(--green)">hello@pineridge-homes.test</div>

<div class="field" style="top:3867px;height:60px">Name</div>
<div class="field" style="top:3941px;height:60px">Email</div>
<div class="field" style="top:4015px;height:105px">Message</div>
<div class="btn send-cta">SEND MESSAGE</div>

<footer class="footer">
  <div class="brand"><span class="brand-mark"></span>PINE RIDGE</div>
  <p class="footer-text">Lorem ipsum, or lipsum as it is sometimes known, is dummy text used in laying out print, graphic or web designs. The passage is attributed</p>
  <div class="copyright">Copyright 2021 Pine Ridge</div>
  <div class="footer-head" style="left:536px">Quick Links</div>
  <ul class="quick"><li>Home</li><li>About</li><li>Services</li><li>Portfolio</li><li>Team</li><li>Contact Us</li></ul>
  <div class="footer-head" style="left:811px">Contact Us</div>
  <svg class="abs" style="left:811px;top:134px" width="13" height="15" viewBox="0 0 16 18"><path d="M8 1C4.7 1 2 3.6 2 6.8 2 11 8 17 8 17s6-6 6-10.2C14 3.6 11.3 1 8 1z" fill="none" stroke="#d7dadd" stroke-width="1.5"/></svg>
  <div class="footer-contact">Pine Ridge<br>Company Reg: REG-804.217.553<br>Office: Larchweg 14,&nbsp; Talbach, Alpland<br><br>+00 482 55170<br><span style="color:var(--green)">hello@pineridge-homes.test</span></div>
</footer>

</body>
</html>
```